Tender Horizon yoga, meditation & wellness

I teach kundalini yoga and meditation classes.
I have adult beginner classes, seniors classes, family yoga classes, kids yoga classes
I also offer events like cacao ceremony, full moon ceremony, and retreats

Professional, and simple website that is easy to navigate, and easy for me to update, change.

Target Market(s)

all ages

Industry/Entity Type

Health And Wellness

Coding

Coded - Design and coding required

Number of Pages Required

5+ page

Font styles to use
Decorative

Colors
cedeed
eedded
e4daeb
fbd4d5
fee3d4

Requirements
Must have
• tabs required: about, contact, events, classes, blog,
• I would like to link my facebook page & instagram accounts to the website
Nice to have
• I would like my clients to be able to register for classes and events from my website
• I would like to have a "shop" option in the future, for some items that I have for sale

```html
<!DOCTYPE html>
<html lang="en">
<head>
<meta charset="utf-8">
<title>Tender Horizon Yoga</title>
<link href="https://fonts.googleapis.com/css2?family=Oswald:wght@400;500&family=Roboto:wght@300;400;500;700&display=swap" rel="stylesheet">
<style>
:root{
  --ink:#2a2a2a;
  --body:#555;
  --pink:#fbd4d5;
  --pink-deep:#f3a9ac;
  --red:#d9262b;
  --lilac:#e4daeb;
  --lilac-deep:#d9cbe3;
  --grey:#eeeeee;
  --footer:#1d1d1d;
  --white:#fff;
}
*{box-sizing:border-box;margin:0;padding:0}
html,body{width:1200px;height:3863px;overflow:hidden}
body{position:relative;font-family:"Roboto",sans-serif;color:var(--body);background:var(--white)}
.abs{position:absolute}
.photo{position:absolute}

/* header / hero */
.hero{left:0;top:0;width:1200px;height:695px;background:linear-gradient(180deg,#f6f2ef 0%,#e9e0d8 35%,#b9a89a 70%,#7a5f4a 100%)}
.hero-figure{left:330px;top:0;width:440px;height:640px;background:radial-gradient(ellipse at 50% 45%,#f1c9b8 0%,#dba98f 40%,rgba(200,160,140,0) 75%)}
.hero-deck{left:0;top:560px;width:1200px;height:135px;background:linear-gradient(180deg,#9a6e4f,#6a4630)}
.logo{left:142px;top:88px;font-family:"Roboto",sans-serif;font-weight:500;color:#3b3b3b;font-size:22px;letter-spacing:2px;line-height:1.2}
.logo-mark{left:176px;top:30px;width:52px;height:52px;border-radius:50%;background:var(--pink)}
.call{left:535px;top:28px;display:flex;align-items:center;gap:14px}
.call .icon{width:40px;height:40px;border-radius:50%;background:var(--pink);display:flex;align-items:center;justify-content:center}
.call small{display:block;font-size:15px;color:#333}
.call strong{font-size:22px;font-weight:400;color:#333}
.btn-register{left:780px;top:28px;width:152px;height:40px;border:2px solid #333;border-radius:20px;background:#fff;font-size:14px;font-weight:500;color:#333;display:flex;align-items:center;justify-content:center;gap:8px}
.social{width:40px;height:40px;border-radius:50%;background:#3b3b3b}
.nav{left:450px;top:103px;display:flex;gap:0;font-size:17px;font-weight:500;color:#333}
.nav a{text-decoration:none;color:inherit}
.hero-title{left:142px;top:268px;font-family:"Oswald",sans-serif;font-weight:400;font-size:45px;line-height:1.2;color:#222}
.btn-shop{left:145px;top:410px;width:180px;height:46px;border-radius:23px;background:#fff;font-size:17px;font-weight:700;color:#222;display:flex;align-items:center;justify-content:center}
.arrow-btn{width:32px;height:32px;border-radius:50%;background:#333;display:flex;align-items:center;justify-content:center}
.hero-notch{left:0;top:655px;width:1200px;height:60px}

/* welcome */
.welcome-title{left:145px;top:800px;font-size:32px;font-weight:700;color:#333;line-height:1.35;letter-spacing:.5px}
.rule{height:2px;background:linear-gradient(90deg,#333 0 45%,var(--pink) 45%)}
.para{font-size:14px;line-height:2.05;color:#444}
.feature{display:flex;align-items:center;gap:16px;font-size:15px;color:#444;line-height:1.5}
.feature .ring{width:76px;height:76px;border-radius:50%;background:var(--pink)}
.welcome-photo{left:655px;top:760px;width:455px;height:480px;background:radial-gradient(circle at 50% 40%,#f2eef0 0%,#e7e0e6 45%,#fff 70%)}

/* classes */
.classes{left:0;top:1315px;width:1200px;height:740px;background:var(--lilac)}
.sec-title{width:1200px;text-align:center;font-size:36px;color:#222;font-weight:400;letter-spacing:.5px}
.sec-title b{font-weight:700}
.twin-rule{display:flex;justify-content:center;gap:20px}
.twin-rule span{width:60px;height:2px;background:#555}
.lead{left:195px;width:810px;text-align:center;font-size:14px;line-height:2;color:#444}
.class-card{top:1655px;width:287px;height:300px;background:#fff;box-shadow:0 3px 6px rgba(0,0,0,.08);text-align:center}
.class-card h3{margin-top:138px;font-size:18px;font-weight:500;color:#222}
.class-card p{margin:12px 18px 0;font-size:13px;line-height:1.85;color:#555}
.class-photo{width:180px;height:180px;border-radius:50%;border:4px solid #fff}

/* events */
.event-big{left:145px;top:2275px;width:425px;height:330px;background:linear-gradient(160deg,#6b5a44,#3c2e22 60%,#b77a3a)}
.event-caption{left:185px;top:2530px;width:345px;height:90px;background:#fff;text-align:center}
.event-caption h3{margin-top:22px;font-size:17px;font-weight:500;color:#222;letter-spacing:.5px}
.meta{font-size:13px;font-style:italic;color:var(--red);display:flex;gap:28px;justify-content:center;align-items:center}
.meta span{display:flex;align-items:center;gap:6px}
.event-small{left:603px;width:450px;height:200px;border:1px solid #e2e2e2;background:#fff}
.event-small .thumb{position:absolute;left:0;top:0;width:187px;height:198px}
.event-small .body{position:absolute;left:215px;top:30px;width:220px}
.event-small h3{font-size:17px;font-weight:500;color:#222;margin-bottom:14px}
.event-small .meta{justify-content:flex-start}
.event-small p{margin-top:12px;font-size:12.5px;line-height:1.8;color:#555}

/* testimonials */
.testi{left:0;top:2810px;width:1200px;height:455px;background:linear-gradient(90deg,#f1efef,#f6f5f5 60%,#efeded)}
.testi-avatar{left:200px;top:2980px;width:180px;height:180px;border-radius:50%;border:6px solid var(--pink);background:radial-gradient(circle at 50% 40%,#e9c7b4,#b88c72 70%)}

/* footer */
.footer{left:0;top:3265px;width:1200px;height:598px;background:var(--footer)}
.f-title{font-size:22px;color:#fff;font-weight:400}
.f-title b{font-weight:700}
.field{left:148px;width:364px;height:35px;border:1px solid #cfcfcf;font-size:11px;color:#ddd;padding:9px 10px}
.btn-pink{left:148px;top:3648px;width:179px;height:40px;background:var(--pink);color:#333;font-size:15px;font-weight:500;display:flex;align-items:center;justify-content:center}
.contact-row{left:590px;display:flex;gap:22px;font-size:14px;line-height:1.7;color:#eee}
.contact-row .ci{width:30px;height:30px;border-radius:50%;border:1.5px solid #eee;flex:none;display:flex;align-items:center;justify-content:center}
.links{left:918px;top:3425px;font-size:14px;line-height:28px;color:#eee;list-style:none}
.f-social{width:30px;height:30px;border-radius:50%;border:1.5px solid #eee}
.copyright{left:0;top:3795px;width:1200px;text-align:center;font-size:13px;color:#ddd}
</style>
</head>
<body>

<!-- Hero -->
<section class="abs hero" aria-label="Hero">
  <div class="photo" role="img" aria-label="Woman meditating cross-legged on a wooden deck above the sea, glowing chakra points along her spine" style="left:0;top:0;width:1200px;height:695px;background:linear-gradient(180deg,rgba(255,255,255,.55) 0%,rgba(255,255,255,0) 30%)"></div>
  <div class="photo hero-figure" aria-hidden="true"></div>
  <div class="photo hero-deck" aria-hidden="true"></div>
</section>

<div class="abs logo-mark" aria-hidden="true"></div>
<div class="abs logo">TENDER HORIZON<br>YOGA</div>

<div class="abs call">
  <span class="icon"><svg width="18" height="18" viewBox="0 0 24 24"><path d="M6.6 10.8a15 15 0 0 0 6.6 6.6l2.2-2.2a1 1 0 0 1 1-.25 11.4 11.4 0 0 0 3.6.6 1 1 0 0 1 1 1V20a1 1 0 0 1-1 1A17 17 0 0 1 3 4a1 1 0 0 1 1-1h3.5a1 1 0 0 1 1 1c0 1.25.2 2.45.6 3.6a1 1 0 0 1-.25 1z" fill="#d9262b"/></svg></span>
  <span><small>Call Us :</small><strong>555-0142-7788</strong></span>
</div>
<div class="abs btn-register"><svg width="14" height="14" viewBox="0 0 24 24"><path d="M4 20h4l10-10-4-4L4 16z M14 6l4 4" fill="none" stroke="#333" stroke-width="2"/></svg>REGISTER</div>
<div class="abs social" style="left:952px;top:28px" role="img" aria-label="Social profile link"></div>
<div class="abs social" style="left:1012px;top:28px" role="img" aria-label="Photo profile link"></div>

<nav class="abs nav">
  <a style="width:95px">HOME</a><a style="width:100px">ABOUT</a><a style="width:125px">CONTACT</a><a style="width:110px">EVENTS</a><a style="width:125px">CLASSES</a><a>BLOG</a>
</nav>

<h1 class="abs hero-title">Kundalini Yoga and<br>Meditation Classes</h1>
<div class="abs btn-shop">SHOP NOW</div>
<div class="abs arrow-btn" style="left:62px;top:357px"><svg width="12" height="12" viewBox="0 0 12 12"><path d="M8 1 3 6l5 5" fill="none" stroke="#fff" stroke-width="2"/></svg></div>
<div class="abs arrow-btn" style="left:1102px;top:357px"><svg width="12" height="12" viewBox="0 0 12 12"><path d="M4 1l5 5-5 5" fill="none" stroke="#fff" stroke-width="2"/></svg></div>
<svg class="abs hero-notch" viewBox="0 0 1200 60" preserveAspectRatio="none" aria-hidden="true"><path d="M0 40H520C560 40 570 15 600 15S640 40 680 40H1200V60H0z" fill="#fff"/></svg>
<svg class="abs" style="left:588px;top:690px" width="24" height="32" viewBox="0 0 24 32" aria-hidden="true"><path d="M12 2v26M3 19l9 9 9-9" fill="none" stroke="#444" stroke-width="2"/></svg>

<!-- Welcome -->
<h2 class="abs welcome-title">WELCOME TO<br>TENDER HORIZON YOGA</h2>
<div class="abs rule" style="left:145px;top:905px;width:470px"></div>
<p class="abs para" style="left:145px;top:932px;width:475px">Sed ut perspiciatis unde omnis iste natus error sit voluptatem accusantium doloremque laudantium, totam rem aperiam, eaque ipsa quae ab illo inventore veritatis et quasi architecto beatae vitae dicta sunt explicabo. Nemo enim ipsam voluptatem quia voluptas sit aspernatur aut odit aut fugit, sed quia consequuntur magni dolores eos qui ratione voluptatem sequi nesciunt.</p>
<div class="abs feature" style="left:145px;top:1127px"><span class="ring"></span><span>Kundalini<br>yoga</span></div>
<div class="abs feature" style="left:350px;top:1127px"><span class="ring"></span><span>Meditation<br>classes</span></div>
<div class="photo welcome-photo" role="img" aria-label="Woman in white meditating on a round patterned rug with arms raised"></div>

<!-- Classes -->
<section class="abs classes" aria-label="Our classes"></section>
<h2 class="abs sec-title" style="left:0;top:1383px"><b>OUR</b> CLASSES</h2>
<div class="abs twin-rule" style="left:0;top:1460px;width:1200px"><span></span><span></span></div>
<p class="abs lead" style="top:1496px">Lorem ipsum dolor sit amet, consectetuer adipiscing elit, sed diam nonummy nibh euismod tincidunt ut laoreet dolore magna aliquam erat volutpat. Ut wisi enim ad minim veniam, quis nostrud exerci tation</p>

<article class="abs class-card" style="left:145px"><h3>SENIORS CLASSES</h3><p>Sed ut perspiciatis unde omnis iste natus error sit voluptatem accusantium emque laudantium, totam rem aperiam, eaque ipsa quae ab illo inventore</p></article>
<article class="abs class-card" style="left:455px"><h3>FAMILY YOGA CLASSES</h3><p>Sed ut perspiciatis unde omnis iste natus error sit voluptatem accusantium emque laudantium, totam rem aperiam, eaque ipsa quae ab illo inventore</p></article>
<article class="abs class-card" style="left:767px"><h3>KIDS YOGA CLASSES</h3><p>Sed ut perspiciatis unde omnis iste natus error sit voluptatem accusantium emque laudantium, totam rem aperiam, eaque ipsa quae ab illo inventore</p></article>
<div class="photo class-photo" style="left:198px;top:1590px;background:linear-gradient(180deg,#cfe0c0,#8fb07a)" role="img" aria-label="Seniors doing a seated yoga pose outdoors"></div>
<div class="photo class-photo" style="left:508px;top:1590px;background:linear-gradient(180deg,#b9c9c2,#5f7a6a)" role="img" aria-label="Family practising yoga together"></div>
<div class="photo class-photo" style="left:820px;top:1590px;background:linear-gradient(180deg,#d9a99a,#8b4f5a)" role="img" aria-label="Children in a yoga class"></div>

<!-- Events -->
<h2 class="abs sec-title" style="left:0;top:2133px"><b>LATEST</b> EVENTS</h2>
<div class="abs twin-rule" style="left:0;top:2210px;width:1200px"><span></span><span></span></div>

<div class="photo event-big" role="img" aria-label="Seated statue, candle and cacao chocolate on a wooden table"></div>
<div class="abs event-caption">
  <h3>CACAO CEREMONY</h3>
  <div class="meta" style="margin-top:10px">
    <span><svg width="12" height="12" viewBox="0 0 12 12"><rect x="1" y="2" width="10" height="9" fill="none" stroke="#d9262b" stroke-width="1.4"/><path d="M1 5h10" stroke="#d9262b"/></svg>Jan 25, 2018</span>
    <span><svg width="13" height="12" viewBox="0 0 13 12"><path d="M1 2h11v6H5l-3 3V8H1z" fill="none" stroke="#d9262b" stroke-width="1.2"/></svg>2 comments</span>
  </div>
</div>
<p class="abs" style="left:195px;top:2626px;width:330px;text-align:center;font-size:12.5px;line-height:1.8;color:#555">Sed ut perspiciatis unde omnis iste natus error sit voluptatem accusantium doloremque laudantium, totam rem aperiam, eaque ipsa quae ab illo inventore</p>

<article class="abs event-small" style="top:2275px">
  <div class="thumb" role="img" aria-label="Full moon over a temple with rows of candles at night" style="background:linear-gradient(180deg,#1b1e2a,#2d2a2c 60%,#a7641f)"></div>
  <div class="body">
    <h3>FULL MOON CEREMONY</h3>
    <div class="meta"><span><svg width="12" height="12" viewBox="0 0 12 12"><rect x="1" y="2" width="10" height="9" fill="none" stroke="#d9262b" stroke-width="1.4"/></svg>Jan 25, 2018</span><span><svg width="13" height="12" viewBox="0 0 13 12"><path d="M1 2h11v6H5l-3 3V8H1z" fill="none" stroke="#d9262b" stroke-width="1.2"/></svg>2 comments</span></div>
    <p>Sed ut perspiciatis unde omnis iste natus error sit voluptatem accusantium doque laudantium, totam</p>
  </div>
</article>
<article class="abs event-small" style="top:2500px;height:205px">
  <div class="thumb" role="img" aria-label="Woman meditating on a forest veranda" style="height:203px;background:linear-gradient(180deg,#bcc8a8,#6c7a58)"></div>
  <div class="body">
    <h3>RETREATS</h3>
    <div class="meta"><span><svg width="12" height="12" viewBox="0 0 12 12"><rect x="1" y="2" width="10" height="9" fill="none" stroke="#d9262b" stroke-width="1.4"/></svg>Jan 25, 2018</span><span><svg width="13" height="12" viewBox="0 0 13 12"><path d="M1 2h11v6H5l-3 3V8H1z" fill="none" stroke="#d9262b" stroke-width="1.2"/></svg>2 comments</span></div>
    <p>Sed ut perspiciatis unde omnis iste natus error sit voluptatem accusantium doque laudantium, totam</p>
  </div>
</article>

<!-- Testimonials -->
<section class="abs testi" aria-label="Testimonials"></section>
<svg class="abs" style="left:188px;top:2885px" width="160" height="130" viewBox="0 0 160 130" aria-hidden="true"><path d="M0 0h70v60L40 130H10l20-70H0zM88 0h70v60l-30 70H98l20-70H88z" fill="#f5c9cb" opacity=".8"/></svg>
<div class="photo testi-avatar" role="img" aria-label="Portrait of a smiling client"></div>
<h2 class="abs" style="left:423px;top:2910px;font-size:34px;font-weight:700;color:#222">TESTIMONIES</h2>
<p class="abs" style="left:423px;top:2972px;width:595px;font-size:15.5px;line-height:1.95;color:#444">Sed ut perspiciatis unde omnis iste natus error sit voluptatem accusantium doloremque laudantium, totam rem aperiam, eaque ipsa quae ab illo inventore veritatis et quasi architecto beatae vitae dicta sunt explicabo. Nemo enim ipsam voluptatem quia voluptas sit aspernatur aut odit aut fugit, sed quia consequuntur magni dolores eos qui ratione</p>
<p class="abs" style="left:423px;top:3137px;font-size:15px;color:#333">Maya Collins, Tender Horizon Yoga</p>
<svg class="abs" style="left:970px;top:3118px" width="36" height="30" viewBox="0 0 36 30" aria-hidden="true"><path d="M12 3 2 15l10 12M24 3l10 12-10 12" fill="none" stroke="#ccc" stroke-width="1.5"/></svg>

<!-- Footer -->
<footer class="abs footer" aria-label="Footer"></footer>
<svg class="abs" style="left:0;top:3245px" width="1200" height="40" viewBox="0 0 1200 40" aria-hidden="true"><path d="M0 20H530C570 20 575 0 600 0S630 20 670 20H1200V40H0z" fill="#1d1d1d"/></svg>
<svg class="abs" style="left:594px;top:3258px" width="24" height="32" viewBox="0 0 24 32" aria-hidden="true"><path d="M12 30V4M3 13l9-9 9 9" fill="none" stroke="#fff" stroke-width="2"/></svg>

<h3 class="abs f-title" style="left:148px;top:3343px"><b>EMAIL</b> US</h3>
<div class="abs field" style="top:3437px">First Name</div>
<div class="abs field" style="top:3482px">Email Address</div>
<div class="abs field" style="top:3527px">Phone Number</div>
<div class="abs field" style="top:3572px;height:60px">Message :</div>
<div class="abs btn-pink">REGISTER</div>

<h3 class="abs f-title" style="left:587px;top:3343px"><b>CONTACT</b> US</h3>
<div class="abs contact-row" style="top:3430px"><span class="ci"><svg width="12" height="14" viewBox="0 0 12 14"><path d="M6 13S1 8 1 5a5 5 0 0 1 10 0c0 3-5 8-5 8z" fill="none" stroke="#eee" stroke-width="1.3"/><circle cx="6" cy="5" r="1.6" fill="#eee"/></svg></span><span>Tender Horizon Yoga<br>Willow Lane 14, 2nd Floor,<br>PO Box – 2207</span></div>
<div class="abs contact-row" style="top:3512px"><span class="ci"><svg width="13" height="13" viewBox="0 0 24 24"><path d="M6.6 10.8a15 15 0 0 0 6.6 6.6l2.2-2.2 4.6 1.4V20A17 17 0 0 1 3 4h3.5l1.4 4.6z" fill="#eee"/></svg></span><span>Phone: +555 0190 4421<br>Mobile: 555 01 334 2290</span></div>
<div class="abs contact-row" style="top:3580px"><span class="ci"><svg width="13" height="10" viewBox="0 0 13 10"><rect x=".7" y=".7" width="11.6" height="8.6" fill="none" stroke="#eee" stroke-width="1.2"/><path d="M1 1l5.5 4.5L12 1" fill="none" stroke="#eee" stroke-width="1.2"/></svg></span><span style="line-height:30px">hello@tenderhorizonyoga.com</span></div>
<div class="abs f-social" style="left:592px;top:3635px" role="img" aria-label="Social profile link"></div>
<div class="abs f-social" style="left:633px;top:3635px" role="img" aria-label="Photo profile link"></div>

<h3 class="abs f-title" style="left:918px;top:3343px"><b>QUICK LINKS</b></h3>
<ul class="abs links"><li>Home</li><li>About</li><li>Contact</li><li>Events</li><li>Classes</li><li>Blog</li></ul>

<div class="abs" style="left:148px;top:3755px;width:905px;height:1px;background:#3a3a3a"></div>
<p class="abs copyright">© Copyright 2018 Tender Horizon Yoga. All Rights Reserved.</p>

</body>
</html>
```